Gleam Forge
Clean Car Specialist
Thanks all for the designs. Feel free to use any color combo you'd like in your designs. The red is good but would be good to see some other ideas. Thanks.
Draft #15 - I like the reflection image of the GF on the business card. It really makes it stand out.
Thanks to all the designers for submitting there ideas so far. Please keep them coming.
Note to all designers. I would like to ask that you leave the address OFF the business card and stationery. This may seem strange but I only need the phone number, email and web site included. Thank you.
To all designers - I have uploaded .AI files for your convenience. Thank you.

```html
<!DOCTYPE html>
<html lang="en">
<head>
<meta charset="UTF-8">
<title>Gleam Forge – Business Card</title>
<link href="https://fonts.googleapis.com/css2?family=Open+Sans:wght@400;700;800&display=swap" rel="stylesheet">
<style>
  :root {
    --page: #ffffff;
    --card-dark: #0d0d0d;
    --card-mid: #2b2b2b;
    --band-light: #5a5a5a;
    --band-dark: #333333;
    --brand-red: #d0141c;
    --text-white: #ffffff;
    --faint-red: rgba(190, 20, 28, 0.28);
  }
  html, body {
    margin: 0;
    padding: 0;
    width: 1200px;
    height: 751px;
    overflow: hidden;
    background: var(--page);
    font-family: "Open Sans", Arial, sans-serif;
  }
  .canvas {
    position: relative;
    width: 1200px;
    height: 751px;
  }
  .card {
    position: absolute;
    left: 319px;
    width: 562px;
    height: 336px;
    overflow: hidden;
    background: linear-gradient(180deg, var(--card-mid) 0%, var(--card-dark) 55%, #1c1c1c 100%);
  }
  .card--front { top: 7px; }
  .card--back { top: 403px; }

  .front-mark {
    position: absolute;
    left: 0;
    right: 0;
    top: 105px;
    margin: 0;
    text-align: center;
    font-size: 110px;
    font-weight: 800;
    line-height: 1;
    letter-spacing: -4px;
    color: var(--brand-red);
  }
  .front-web {
    position: absolute;
    left: 0;
    right: 0;
    top: 299px;
    margin: 0;
    text-align: center;
    font-size: 21px;
    font-weight: 700;
    color: var(--text-white);
  }

  .back-band {
    position: absolute;
    left: 0;
    right: 0;
    top: 178px;
    bottom: 0;
    background: linear-gradient(180deg, var(--band-light) 0%, var(--band-dark) 100%);
  }
  .back-logo {
    position: absolute;
    left: 0;
    right: 0;
    top: 22px;
    text-align: center;
  }
  .back-logo__mark {
    margin: 0;
    font-size: 62px;
    font-weight: 800;
    line-height: 1;
    letter-spacing: -2px;
    color: var(--brand-red);
  }
  .back-logo__name {
    margin: 10px 0 0;
    font-size: 19px;
    font-weight: 800;
    letter-spacing: 4px;
    text-transform: uppercase;
    color: var(--brand-red);
  }
  .back-logo__tagline {
    margin: 2px 0 0;
    font-size: 10px;
    font-weight: 700;
    letter-spacing: 3px;
    text-transform: uppercase;
    color: var(--brand-red);
  }
  .back-decor {
    position: absolute;
    left: 310px;
    top: 188px;
    margin: 0;
    font-size: 150px;
    font-weight: 800;
    line-height: 1;
    letter-spacing: -5px;
    color: var(--faint-red);
  }
  .contact {
    position: absolute;
    left: 19px;
    top: 206px;
    color: var(--text-white);
  }
  .contact__name {
    margin: 0 0 4px;
    font-size: 22px;
    font-weight: 700;
  }
  .contact__line {
    margin: 0;
    font-size: 13px;
    font-weight: 700;
    line-height: 1.5;
  }
</style>
</head>
<body>
<main class="canvas">
  <section class="card card--front">
    <p class="front-mark">GF</p>
    <p class="front-web">www.gleamforgekc.com</p>
  </section>

  <section class="card card--back">
    <div class="back-band"></div>
    <div class="back-logo">
      <p class="back-logo__mark">GF</p>
      <p class="back-logo__name">Gleam Forge</p>
      <p class="back-logo__tagline">Clean Car Specialist</p>
    </div>
    <p class="back-decor" aria-hidden="true">GF</p>
    <div class="contact">
      <p class="contact__name">Rhett Calder</p>
      <p class="contact__line">Call: (913)555-0182</p>
      <p class="contact__line">Email: rhett@gleamforgekc.com</p>
    </div>
  </section>
</main>
</body>
</html>
```